Girls & Tween Birthday Hotspot

Looking to refresh our old business cards. We are a girls/tween birthday party store and salon specializing in princess, glamour and spa parties. I would like to maintain the same colors (hot pink and turquoise). Would like the card to be feminine, fun and glitzy..

Target Market(s)

Parents of girls and girls aged 4-14

Industry/Entity Type

Store

Font styles to use
Script

Colors
e34197
85cae6

Requirements
Must have
• name phone and address
colors of hot pink and turquoise
appointment day and time field on one side
Nice to have
• creativity
Should not have
• picture of lipstick

```html
<!DOCTYPE html>
<html lang="en">
<head>
<meta charset="utf-8">
<title>Tiara Lane – Business Cards</title>
<link rel="stylesheet" href="https://fonts.googleapis.com/css2?family=Dancing+Script:wght@700&family=Montserrat:wght@600;700&family=Open+Sans:wght@400;600&display=swap">
<style>
  :root {
    --page-bg: #f3eef2;
    --hot-pink: #e34197;
    --hot-pink-deep: #c92f82;
    --turquoise: #85cae6;
    --turquoise-deep: #69b9da;
    --ribbon: #ffffff;
    --ribbon-fold: #c7a9bb;
    --ink-light: #ffffff;
    --ink-plum: #4a1838;
    --rule: rgba(255,255,255,.85);
  }
  * { box-sizing: border-box; margin: 0; padding: 0; }
  html, body { width: 1000px; height: 1200px; overflow: hidden; }
  body { background: var(--page-bg); position: relative; font-family: "Open Sans", Arial, sans-serif; }

  .card {
    position: absolute; left: 50px; width: 900px; height: 536px; overflow: hidden;
    background: radial-gradient(circle at 25% 30%, var(--hot-pink) 0%, var(--hot-pink-deep) 100%);
    box-shadow: 0 6px 18px rgba(74,24,56,.2);
  }
  .card--front { top: 40px; }
  .card--back  { top: 624px; }

  .turquoise-panel {
    position: absolute; top: 0; bottom: 0;
    background: linear-gradient(180deg, var(--turquoise) 0%, var(--turquoise-deep) 100%);
  }
  .card--front .turquoise-panel { left: 437px; right: 0; }
  .card--back .turquoise-panel { left: 217px; width: 466px; }

  .brand-mark {
    position: absolute; display: flex; align-items: center; justify-content: center; gap: 10px;
    font-family: "Montserrat", Arial, sans-serif; font-weight: 700;
    color: var(--ink-plum); letter-spacing: 3px; font-size: 20px;
  }
  .brand-mark__dot { width: 16px; height: 16px; border-radius: 50%; background: var(--hot-pink); }
  .card--front .brand-mark { left: 437px; right: 0; top: 90px; }
  .card--back .brand-mark { left: 217px; width: 466px; top: 52px; }

  .person { position: absolute; left: 437px; right: 0; text-align: center; }
  .person__name {
    position: absolute; left: 0; right: 0; top: 178px;
    font-family: "Dancing Script", cursive; font-weight: 700; font-size: 60px; line-height: 72px;
    color: var(--ink-light); text-shadow: 0 2px 4px rgba(74,24,56,.35);
  }
  .person__role {
    position: absolute; left: 0; right: 0; top: 256px;
    font-family: "Montserrat", Arial, sans-serif; font-weight: 600; font-size: 17px;
    color: var(--ink-plum); letter-spacing: 1px;
  }

  .ribbon {
    position: absolute; background: var(--ribbon); height: 50px;
    display: flex; align-items: center;
    font-family: "Montserrat", Arial, sans-serif; font-weight: 700; font-size: 22px;
    color: var(--hot-pink); letter-spacing: 1px;
    box-shadow: 0 4px 8px rgba(74,24,56,.25);
  }
  .ribbon::after {
    content: ""; position: absolute; left: 0; bottom: -14px;
    border-top: 14px solid var(--ribbon-fold); border-left: 14px solid transparent;
  }
  .card--front .ribbon { left: 420px; right: 0; top: 303px; padding-left: 42px; }
  .card--back .ribbon { left: 160px; width: 580px; top: 398px; justify-content: center; }
  .card--back .ribbon::before {
    content: ""; position: absolute; right: 0; bottom: -14px;
    border-top: 14px solid var(--ribbon-fold); border-right: 14px solid transparent;
  }

  .web {
    position: absolute; color: var(--ink-plum); font-family: "Montserrat", Arial, sans-serif;
    font-weight: 600; font-size: 16px; letter-spacing: 1px; text-align: center;
  }
  .card--front .web { left: 437px; right: 0; top: 374px; }
  .card--back .web { left: 217px; width: 466px; top: 468px; }

  .store { position: absolute; left: 217px; width: 466px; text-align: center; }
  .store__name {
    position: absolute; left: 0; right: 0; top: 84px;
    font-family: "Dancing Script", cursive; font-weight: 700; font-size: 58px; line-height: 70px;
    color: var(--ink-light); text-shadow: 0 2px 4px rgba(74,24,56,.35);
  }
  .store__slogan {
    position: absolute; left: 0; right: 0; top: 160px;
    font-family: "Montserrat", Arial, sans-serif; font-weight: 600; font-size: 14px;
    letter-spacing: 3px; color: var(--ink-plum);
  }

  .appointment {
    position: absolute; left: 277px; width: 346px; top: 206px; height: 160px;
    background: rgba(255,255,255,.9); border: 2px solid var(--hot-pink);
    padding: 14px 26px; color: var(--ink-plum);
  }
  .appointment__title {
    font-family: "Dancing Script", cursive; font-weight: 700; font-size: 30px; line-height: 36px;
    color: var(--hot-pink); text-align: center;
  }
  .appointment__field {
    display: flex; align-items: flex-end; gap: 10px; margin-top: 14px;
    font-family: "Montserrat", Arial, sans-serif; font-weight: 600; font-size: 15px; letter-spacing: 1px;
  }
  .appointment__label { width: 48px; }
  .appointment__line { flex: 1; border-bottom: 2px solid var(--hot-pink); height: 18px; }

  .contact { position: absolute; left: 88px; width: 300px; color: var(--ink-light); font-size: 17px; line-height: 27px; }
  .contact__icon { position: absolute; left: 88px; width: 24px; height: 22px; fill: var(--ink-light); }
  .contact__rule { position: absolute; left: 88px; width: 287px; height: 2px; background: var(--rule); }
</style>
</head>
<body>

<section class="card card--front" aria-label="Business card front">
  <div class="turquoise-panel"></div>

  <svg class="contact__icon" style="top:118px" viewBox="0 0 24 22" aria-hidden="true">
    <path d="M12 1 1 11h3v10h6v-6h4v6h6V11h3z"/>
  </svg>
  <div class="contact__rule" style="top:146px"></div>
  <p class="contact" style="top:157px">48 Maple Lane,<br>Riverton 54321</p>

  <svg class="contact__icon" style="top:222px" viewBox="0 0 24 22" aria-hidden="true">
    <path d="M2 7c0-3 4-5 10-5s10 2 10 5v2h-5V7H7v2H2z"/>
    <path d="M6 10h12l3 10H3z"/>
  </svg>
  <div class="contact__rule" style="top:252px"></div>
  <p class="contact" style="top:262px">555-014-2290<br>555-014-2291</p>

  <svg class="contact__icon" style="top:326px" viewBox="0 0 24 22" aria-hidden="true">
    <path d="M1 1h22v15H1zm2 2v11h18V3z"/>
    <path d="M9 16h6v3h3v2H6v-2h3z"/>
  </svg>
  <div class="contact__rule" style="top:357px"></div>
  <p class="contact" style="top:370px">hello@tiaralaneparty.com<br>www.tiaralaneparty.com</p>

  <div class="brand-mark"><span class="brand-mark__dot"></span>TIARA LANE</div>

  <div class="person">
    <h1 class="person__name">Ella Marsh</h1>
    <p class="person__role">party planner &amp; stylist</p>
  </div>

  <div class="ribbon">PRINCESS · GLAMOUR · SPA</div>
  <p class="web">WWW.TIARALANEPARTY.COM</p>
</section>

<section class="card card--back" aria-label="Business card back">
  <div class="turquoise-panel"></div>
  <div class="brand-mark"><span class="brand-mark__dot"></span>TIARA LANE</div>
  <div class="store">
    <h2 class="store__name">Tiara Lane</h2>
    <p class="store__slogan">BIRTHDAY PARTIES &amp; SALON</p>
  </div>

  <div class="appointment">
    <p class="appointment__title">Your Appointment</p>
    <div class="appointment__field"><span class="appointment__label">DAY</span><span class="appointment__line"></span></div>
    <div class="appointment__field"><span class="appointment__label">TIME</span><span class="appointment__line"></span></div>
  </div>

  <div class="ribbon">PRINCESS · GLAMOUR · SPA</div>
  <p class="web">WWW.TIARALANEPARTY.COM</p>
</section>

</body>
</html>
```